ご覧いただきまして、有難うございます!

制作イメージなどの詳細を記載しております依頼書を以下URLからダウンロードしてご確認頂けますと幸いです。
(依頼書の格納フォルダ)
https://files.morvendale.net/share/folders/7QxT3pN8vLc2Hs5KdW9yRb4ZmE1uGoFaJ?mode=view

継続的にデザインの改修を予定しておりまして、継続的にページのデザイン制作をしていただける方を探しております。長期的な関係を築ければと思います。

上記URL先に格納しております依頼書をお読み頂き、ご質問等ありましたら、気軽にお問い合わせください。
たくさんのご応募をお待ちしております!
依頼書は以下格納フォルダからご確認をお願いします。
(依頼書の格納フォルダ)
• モバイルファースト・レスポンシブWebデザイン対応(モバイル用とPC用を納品)
緑系、青系
難しい要望とは認識しておりますが、良いものを作りたく、何卒よろしくお願いいたします。
ご覧いただきまして、有難うございます!

(依頼書の格納フォルダ)

たくさんのご応募をお待ちしております!

どれもとても良いFVでご提案ありがとうございます。
デザインイメージの中でも、ポジティブな、透明性のあるの2点が特徴的であったため、今回はこちらの提案を選ばせて下さい。

どれもとても良いFVのデザインのご提案ありがとうございます。
社内や外部でも感想を聞く中で、皆様の1つ1つのご提案が大変好評でした。

皆様、お忙しい中で数ある提案依頼がある中で、こちらへご提案を下さり大変感謝しております。次回の製作依頼の際も、ぜひ参加してもらえるとありがたいです。
どうもありがとうございました。

```html
<!DOCTYPE html>
<html lang="ja">
<head>
<meta charset="UTF-8">
<title>個別指導 ミドリ塾</title>
<link rel="stylesheet" href="https://fonts.googleapis.com/css2?family=Noto+Sans+JP:wght@400;500;700;900&display=swap">
<style>
:root{
  --green:#1f8a4d;
  --green-dark:#17713e;
  --green-pale:#e6f3e9;
  --ink:#2a3230;
  --blue:#2b7fd8;
  --yellow:#ffe45c;
  --hero-bg:#eef0ef;
  --white:#ffffff;
  --nav:#222c38;
  --photo-a:#c9c4bc;
  --photo-b:#9aa3a6;
}
*{box-sizing:border-box;margin:0;padding:0}
html,body{width:678px;height:1200px;overflow:hidden}
body{font-family:"Noto Sans JP",sans-serif;color:var(--ink);background:var(--white);position:relative}
.site-header{position:absolute;top:0;left:0;width:678px;height:104px;background:var(--white);display:flex;align-items:center;justify-content:space-between;padding:0 26px}
.brand{display:flex;align-items:center;gap:14px}
.brand-mark{width:22px;height:22px;background:var(--green);border-radius:4px}
.brand-name{font-size:32px;font-weight:900;color:var(--green);letter-spacing:2px}
.brand-sub{font-size:20px;font-weight:900;color:var(--green);letter-spacing:1px}
.header-cta{width:212px;height:62px;border-radius:31px;background:var(--green);color:var(--white);font-size:21px;font-weight:700;display:flex;align-items:center;justify-content:center;gap:18px}
.hero{position:absolute;top:104px;left:0;width:678px;height:796px;background:var(--hero-bg)}
.photo{position:absolute;background:linear-gradient(135deg,var(--photo-a),var(--photo-b))}
.photo-classroom{left:56px;top:40px;width:250px;height:190px}
.photo-lecture{left:232px;top:14px;width:120px;height:110px}
.photo-teacher{left:566px;top:130px;width:112px;height:130px}
.photo-study{left:0;top:470px;width:150px;height:200px}
.photo-booths{left:520px;top:490px;width:158px;height:170px}
.stat-badge{position:absolute;left:400px;top:36px;width:172px;height:172px;border-radius:50%;background:var(--blue);color:var(--white);text-align:center;display:flex;flex-direction:column;align-items:center;justify-content:center;white-space:nowrap;box-shadow:0 6px 14px rgba(0,0,0,.12)}
.stat-badge .line1{font-size:17px;font-weight:700;line-height:1.3}
.stat-badge .line1 em{font-style:normal;color:var(--yellow)}
.stat-badge .line2{font-size:40px;font-weight:900;line-height:1.1;letter-spacing:-1px}
.stat-badge .line2 small{font-size:28px;letter-spacing:0}
.stat-badge .line3{font-size:22px;font-weight:900;line-height:1.2}
.headline{position:absolute;top:280px;left:0;width:678px;text-align:center}
.headline .target{font-size:66px;font-weight:900;color:var(--green);letter-spacing:4px;line-height:1.2}
.headline .aim{font-size:60px;font-weight:900;color:var(--ink);letter-spacing:4px;line-height:1.35}
.headline .aim small{font-size:44px}
.headline .aim b{color:var(--green)}
.price-box{position:absolute;left:192px;top:476px;width:294px;height:146px;background:var(--white);border-radius:6px;text-align:center;padding-top:22px;box-shadow:0 4px 12px rgba(0,0,0,.08)}
.price-box .scope{font-size:26px;font-weight:700;color:var(--ink)}
.price-box .scope b{color:var(--blue);font-size:34px}
.price-box .price{display:flex;align-items:baseline;justify-content:center;gap:6px;margin-top:4px;white-space:nowrap}
.price-box .per{font-size:16px;font-weight:700;writing-mode:vertical-rl;color:var(--blue)}
.price-box .amount{font-size:46px;font-weight:900;color:var(--blue)}
.price-box .tax{font-size:20px;font-weight:700;color:var(--blue)}
.main-cta{position:absolute;left:90px;top:686px;width:494px;height:96px;border-radius:48px;background:var(--green);color:var(--white);font-size:29px;font-weight:700;display:flex;align-items:center;justify-content:center;box-shadow:0 8px 0 var(--green-dark)}
.main-cta svg{position:absolute;right:38px}
.campaign{position:absolute;top:906px;left:0;width:678px;height:190px;background:var(--green-pale);padding:26px 24px}
.campaign .title{font-size:25px;font-weight:900;color:var(--ink)}
.campaign .offer{font-size:25px;font-weight:900;color:var(--green);margin-top:4px}
.campaign .note{font-size:17px;color:#4a5250;margin-top:12px}
.campaign .more{position:absolute;right:24px;top:62px;width:158px;height:50px;border-radius:25px;background:var(--white);border:2px solid var(--green);color:var(--green);font-size:20px;font-weight:700;display:flex;align-items:center;justify-content:center;gap:10px}
.bottom-nav{position:absolute;bottom:0;left:0;width:678px;height:104px;background:var(--nav);display:flex;justify-content:space-around;align-items:center}
.nav-item{display:flex;flex-direction:column;align-items:center;gap:8px;color:var(--white);font-size:17px;font-weight:700;width:130px;white-space:nowrap}
</style>
</head>
<body>
<header class="site-header">
  <div class="brand">
    <span class="brand-mark"></span>
    <span class="brand-sub">個別指導</span>
    <span class="brand-name">ミドリ塾</span>
  </div>
  <div class="header-cta">お問い合わせ
    <svg width="12" height="18" viewBox="0 0 12 18"><path d="M2 2l7 7-7 7" fill="none" stroke="#fff" stroke-width="3"/></svg>
  </div>
</header>

<section class="hero">
  <div class="photo photo-classroom" role="img" aria-label="教室で個別指導を受ける生徒たちの写真"></div>
  <div class="photo photo-lecture" role="img" aria-label="説明をする講師の写真"></div>
  <div class="photo photo-teacher" role="img" aria-label="授業中の生徒と講師の写真"></div>
  <div class="photo photo-study" role="img" aria-label="講師がノートを見ながら指導する写真"></div>
  <div class="photo photo-booths" role="img" aria-label="個別ブースで学習する生徒の写真"></div>

  <div class="stat-badge">
    <div class="line1"><em>91.4%</em>の生徒が</div>
    <div class="line2">+50<small>点以上</small></div>
    <div class="line3">アップ</div>
  </div>

  <h1 class="headline">
    <div class="target">都立高校上位校</div>
    <div class="aim"><small>を</small><b>目指す</b><small>なら</small></div>
  </h1>

  <div class="price-box">
    <div class="scope"><b>5</b>科目対応で</div>
    <div class="price"><span class="per">月額</span><span class="amount">26,400円</span><span class="tax">(税込)</span></div>
  </div>

  <div class="main-cta">お問い合わせ
    <svg width="14" height="22" viewBox="0 0 14 22"><path d="M3 3l8 8-8 8" fill="none" stroke="#fff" stroke-width="3"/></svg>
  </div>
</section>

<section class="campaign">
  <div class="title">新教室限定 新規開講特典</div>
  <div class="offer">入塾金無料&amp;教材プレゼント!</div>
  <div class="note">2022年に開校した教室限定の入会キャンペーンです。</div>
  <div class="more">詳しく見る
    <svg width="10" height="16" viewBox="0 0 10 16"><path d="M2 2l6 6-6 6" fill="none" stroke="#1f8a4d" stroke-width="2.5"/></svg>
  </div>
</section>

<nav class="bottom-nav">
  <div class="nav-item">
    <svg width="34" height="34" viewBox="0 0 24 24" fill="none" stroke="#fff" stroke-width="2"><path d="M3 11l9-8 9 8v10h-6v-6H9v6H3z"/></svg>ホーム</div>
  <div class="nav-item">
    <svg width="34" height="34" viewBox="0 0 24 24" fill="none" stroke="#fff" stroke-width="2"><path d="M5 3l7 9 7-9M12 12v10M6 13h12M6 17h12"/></svg>コース・料金</div>
  <div class="nav-item">
    <svg width="34" height="34" viewBox="0 0 24 24" fill="none" stroke="#fff" stroke-width="2.2"><circle cx="10" cy="10" r="7"/><path d="M15 15l6 6"/></svg>教室を探す</div>
  <div class="nav-item">
    <svg width="34" height="34" viewBox="0 0 24 24" fill="none" stroke="#fff" stroke-width="2"><circle cx="12" cy="12" r="10"/><path d="M9 9a3 3 0 1 1 4 2.8c-.7.3-1 1-1 1.7V14"/><circle cx="12" cy="17.5" r=".6" fill="#fff"/></svg>よくある質問</div>
  <div class="nav-item">
    <svg width="34" height="34" viewBox="0 0 24 24" fill="none" stroke="#fff" stroke-width="2"><path d="M5 2h10l4 4v16H5z"/><path d="M8 10h8M8 14h8M8 18h5"/></svg>ブログ</div>
</nav>
</body>
</html>
```